Maple Ridge business card design

Card needs to include the following text/items:
Company Logo
Tobin Marsh
Phone # - 555-318-7642
service@mapleridgelandscaping.example
Lawn & landscape maintenance services

```html
<!DOCTYPE html>
<html lang="en">
<head>
<meta charset="utf-8">
<title>Maple Ridge Landscaping – Business Card</title>
<link rel="stylesheet" href="https://fonts.googleapis.com/css2?family=Work+Sans:wght@400;500;600&display=swap">
<style>
  :root {
    --backdrop: #36312d;
    --card-paper: #e4eef5;
    --navy: #0f2b3a;
    --brown: #7a4630;
    --brand-green: #1f4a26;
    --ink-dark: #2e3a40;
    --name-tint: #cfe2ee;
    --phone-tint: #f1e6de;
    --mark-fill: #6f9c58;
  }
  * { margin: 0; padding: 0; box-sizing: border-box; }
  html, body { width: 1200px; height: 1000px; overflow: hidden; }
  body {
    background: var(--backdrop);
    font-family: "Work Sans", Arial, sans-serif;
    position: relative;
  }
  .card {
    position: absolute;
    left: 356px;
    width: 490px;
    height: 280px;
    background: var(--card-paper);
    overflow: hidden;
  }
  .card--front { top: 170px; }
  .card--back { top: 539px; }

  .corner-tab { position: absolute; }
  .corner-tab--top-right {
    right: 0; top: 0; width: 97px; height: 44px;
    background: var(--brown);
    border-bottom-left-radius: 44px;
  }
  .corner-tab--bottom-left {
    left: 0; bottom: 0; width: 97px; height: 46px;
    background: var(--navy);
    border-top-right-radius: 46px;
  }

  .brand {
    position: absolute;
    display: flex; flex-direction: column; align-items: center;
  }
  .brand__mark {
    border-radius: 50%;
    background: var(--mark-fill);
  }
  .brand__name {
    color: var(--brand-green);
    font-weight: 600;
    white-space: nowrap;
    letter-spacing: 0.5px;
  }
  .card--front .brand { left: 0; right: 0; top: 76px; }
  .card--front .brand__mark { width: 88px; height: 88px; }
  .card--front .brand__name { font-size: 24px; margin-top: 12px; }

  .email {
    position: absolute; left: 0; right: 0; top: 217px;
    text-align: center;
    font-size: 13px;
    color: var(--brown);
  }

  .back__left {
    position: absolute; left: 0; top: 0; width: 274px; height: 280px;
  }
  .card--back .brand { left: 0; right: 0; top: 82px; }
  .card--back .brand__mark { width: 72px; height: 72px; }
  .card--back .brand__name { font-size: 20px; margin-top: 10px; }
  .tagline {
    position: absolute; left: 0; right: 0; top: 203px;
    text-align: center;
    font-size: 10.5px;
    color: var(--ink-dark);
  }
  .back__name-panel {
    position: absolute; left: 274px; top: 0; width: 216px; height: 142px;
    background: var(--navy);
  }
  .holder-name {
    position: absolute; left: 60px; top: 38px;
    font-size: 26px; line-height: 32px;
    font-weight: 400;
    color: var(--name-tint);
  }
  .back__contact-panel {
    position: absolute; left: 274px; top: 142px; width: 216px; height: 138px;
    background: var(--brown);
  }
  .phone {
    position: absolute; left: 38px; top: 60px;
    display: flex; align-items: center; gap: 4px;
    font-size: 15px;
    color: var(--phone-tint);
  }
  .phone svg { width: 17px; height: 17px; }
</style>
</head>
<body>
  <section class="card card--front">
    <div class="corner-tab corner-tab--top-right"></div>
    <div class="corner-tab corner-tab--bottom-left"></div>
    <div class="brand">
      <div class="brand__mark"></div>
      <div class="brand__name">Maple Ridge</div>
    </div>
    <p class="email">service@mapleridgelandscaping.example</p>
  </section>

  <section class="card card--back">
    <div class="back__left">
      <div class="brand">
        <div class="brand__mark"></div>
        <div class="brand__name">Maple Ridge</div>
      </div>
      <p class="tagline">Lawn &amp; landscape maintenance services</p>
    </div>
    <div class="back__name-panel">
      <h1 class="holder-name">Tobin<br>Marsh</h1>
    </div>
    <div class="back__contact-panel">
      <p class="phone">
        <svg viewBox="0 0 24 24" fill="none" stroke="currentColor" stroke-width="1.8" aria-hidden="true">
          <circle cx="12" cy="12" r="10.5"/>
          <path d="M8.6 6.8c.4-.3 1-.3 1.3.2l1.1 1.8c.2.4.1.9-.2 1.2l-.7.6c.6 1.3 1.6 2.4 2.9 3l.6-.7c.3-.3.8-.4 1.2-.2l1.8 1.1c.5.3.5.9.2 1.3l-.8.9c-.6.6-1.5.8-2.3.4-2.7-1.2-4.8-3.3-6-6-.4-.8-.2-1.7.4-2.3z"/>
        </svg>
        555-318-7642
      </p>
    </div>
  </section>
</body>
</html>
```